Startup online payment business - Sporting / Golf, Swift Tee payment

Background:
Our business name is "Swift Tee" we provide online payments for golfing services via our website. We currently have a logo used on our website. No other design style has been developed. Our aim is to remove cash payments for service at golf clubs.

Our Key Values:
Quick and easy
Formal and polite
Fun with professional boundary
Mate-ship relationships
100% online digital

What we want from you:
Marketing design to be used on posters and stickers in a retail setting to direct customers to our online payment Chanel.
Design must incorporate attached logo, URL swifttee.com.au and our key values can act as a guide the type of design. We have used color Hex#007672 for logo background. We are open to use other colors.

Target Market(s)

Golf clubs and golf players

Industry/Entity Type

Golf Course

Font styles to use
Sans Serif

Requirements
Must have
• Directions to online payment via URL: swifttee.com.au
Nice to have
• We like the idea of the slogan: No Cash - No worries. Have attached home screen that will be available from URL link. Consideration if using mobile phone in image. Push the online payment and steps 1. Visit swifttee.com 2. Select club 3. Confirm payment
Should not have
• Cartoons

```html
<!DOCTYPE html>
<html lang="en">
<head>
<meta charset="utf-8">
<title>Swift Tee – Poster</title>
<link rel="stylesheet" href="https://fonts.googleapis.com/css2?family=Ubuntu:ital,wght@0,400;0,500;0,700;1,400;1,500&family=Source+Sans+3:ital,wght@0,400;0,600;0,700;1,600&display=swap">
<style>
  :root{
    --teal:#007672;
    --teal-dark:#06625f;
    --green:#5f9a2e;
    --green-light:#76a83c;
    --cream:#f4f2bd;
    --cream-deep:#eceaa9;
    --white:#ffffff;
    --canvas:#dcdcbc;
  }
  *{box-sizing:border-box;margin:0;padding:0}
  html,body{width:1200px;height:1200px;overflow:hidden;background:var(--canvas)}
  .poster{
    position:absolute;left:190px;top:27px;width:820px;height:1146px;overflow:hidden;
    background:linear-gradient(180deg,var(--cream) 0%,var(--cream-deep) 60%);
    font-family:"Ubuntu",sans-serif;color:var(--teal);
  }
  .course-photo{
    position:absolute;left:0;top:690px;width:820px;height:456px;
    background:linear-gradient(180deg,rgba(236,234,169,0) 0%,#c9d27a 25%,#a9c45a 50%,#79a93a 75%,#5d952c 100%);
  }
  .shapes{position:absolute;left:0;top:0}
  .brand-tab{
    position:absolute;left:30px;top:0;width:237px;height:170px;
    display:flex;align-items:center;justify-content:center;
  }
  .brand-name{font-family:"Ubuntu",sans-serif;font-weight:500;font-size:40px;color:var(--white);letter-spacing:1px}
  .values-title{
    position:absolute;left:63px;top:205px;
    font-family:"Source Sans 3",sans-serif;font-weight:700;font-size:36px;text-decoration:underline;text-underline-offset:4px;
  }
  .values-list{position:absolute;left:62px;top:272px;list-style:none}
  .values-list li{display:flex;align-items:center;height:44px;font-size:26px;font-weight:500}
  .values-list svg{flex:none}
  .value-icon{width:36px;height:36px;margin-right:20px}
  .value-arrow{width:28px;height:12px;margin-right:12px}
  .intro{
    position:absolute;right:80px;top:84px;text-align:right;
    font-family:"Source Sans 3",sans-serif;font-style:italic;font-weight:600;font-size:26px;line-height:37px;color:var(--white);
  }
  .digital-badge{
    position:absolute;left:575px;top:330px;width:240px;text-align:center;color:var(--white);
  }
  .digital-badge .percent{font-family:"Source Sans 3",sans-serif;font-weight:700;font-size:30px;line-height:34px}
  .digital-badge .label{font-family:"Source Sans 3",sans-serif;font-style:italic;font-size:23px;margin-top:2px}
  .phone-mockup{
    position:absolute;left:37px;top:463px;width:135px;height:275px;border-radius:20px;
    background:linear-gradient(180deg,#e9ecee,#c9ced2);
  }
  .phone-mockup::after{content:"";position:absolute;left:9px;top:36px;right:9px;bottom:36px;background:var(--teal);border-radius:2px}
  .steps{position:absolute;left:191px;top:525px;color:var(--white);font-family:"Source Sans 3",sans-serif}
  .steps h2{font-weight:700;font-size:29px;margin-bottom:14px}
  .steps ol{list-style:none;font-size:22px}
  .steps li{height:38.5px;display:flex}
  .steps .num{width:38px}
  .slogan{
    position:absolute;left:0;width:820px;top:786px;text-align:center;
    font-family:"Ubuntu",sans-serif;font-weight:700;font-size:38px;font-variant:small-caps;letter-spacing:3px;
  }
  .url-pill{
    position:absolute;left:175px;top:880px;width:466px;height:57px;border-radius:29px;background:var(--teal);
    display:flex;align-items:center;justify-content:center;
    color:var(--white);font-weight:700;font-size:28px;letter-spacing:12px;padding-left:12px;
  }
</style>
</head>
<body>
<main class="poster">
  <div class="course-photo" role="img" aria-label="Sunlit golf course fairway with a golf ball and iron club on the grass"></div>

  <svg class="shapes" width="820" height="1146" viewBox="0 0 820 1146" aria-hidden="true">
    <rect x="47" y="26" width="726" height="1091" fill="none" stroke="var(--white)" stroke-width="3"/>
    <!-- brand tab -->
    <path d="M30,0 H267 V170 Q200,150 140,172 Q80,192 36,178 Q30,176 30,166 Z" fill="var(--teal)"/>
    <!-- intro banner -->
    <path d="M398,128 Q392,110 414,117 L720,268 L590,300 Q560,308 530,290 Z" fill="var(--teal)"/>
    <path d="M432,59 H820 V283 H560 Q528,283 508,258 L405,100 Q390,60 432,59 Z" fill="var(--green)"/>
    <!-- digital badge -->
    <path d="M600,328 H820 V460 H556 Q536,460 548,442 L585,345 Q592,328 600,328 Z" fill="var(--teal)"/>
    <circle cx="695" cy="398" r="27" fill="var(--green-light)" stroke="var(--cream)" stroke-width="2"/>
    <rect x="685" y="383" width="18" height="30" rx="3" fill="none" stroke="var(--white)" stroke-width="2"/>
    <rect x="694" y="391" width="16" height="10" fill="var(--green-light)" stroke="var(--white)" stroke-width="2"/>
    <!-- steps band -->
    <path d="M0,540 H772 Q800,540 782,568 L688,716 Q662,755 612,755 H0 Z" fill="var(--teal)"/>
    <path d="M0,499 H738 Q762,499 752,522 L668,680 Q646,712 606,712 H0 Z" fill="var(--green-light)"/>
  </svg>

  <div class="brand-tab"><span class="brand-name">Swift Tee</span></div>

  <p class="intro">We provide<br>online payments<br>for golfing services<br>via our website</p>

  <h1 class="values-title">Our Key Values:</h1>
  <ul class="values-list">
    <li>
      <svg class="value-icon" viewBox="0 0 36 36"><circle cx="18" cy="20" r="12" fill="none" stroke="var(--teal)" stroke-width="2"/><path d="M18 4v4M15 4h6M18 20l5-5" stroke="var(--teal)" stroke-width="2" fill="none"/></svg>
      <svg class="value-arrow" viewBox="0 0 28 12"><path d="M0 0 L28 6 L0 12 L5 6 Z" fill="var(--teal)"/></svg>Quick and easy
    </li>
    <li>
      <svg class="value-icon" viewBox="0 0 36 36"><path d="M14 4h8l-2 5 4 20-6 5-6-5 4-20z" fill="none" stroke="var(--teal)" stroke-width="2"/></svg>
      <svg class="value-arrow" viewBox="0 0 28 12"><path d="M0 0 L28 6 L0 12 L5 6 Z" fill="var(--teal)"/></svg>Formal and polite
    </li>
    <li>
      <svg class="value-icon" viewBox="0 0 36 36"><path d="M18 10l2 6 6 2-6 2-2 6-2-6-6-2 6-2z" fill="var(--teal)"/><circle cx="8" cy="8" r="2" fill="var(--teal)"/><circle cx="29" cy="9" r="2" fill="var(--teal)"/><circle cx="28" cy="28" r="2" fill="var(--teal)"/></svg>
      <svg class="value-arrow" viewBox="0 0 28 12"><path d="M0 0 L28 6 L0 12 L5 6 Z" fill="var(--teal)"/></svg>Fun with professional boundary
    </li>
    <li>
      <svg class="value-icon" viewBox="0 0 36 36"><circle cx="12" cy="11" r="5" fill="none" stroke="var(--teal)" stroke-width="2"/><circle cx="24" cy="11" r="5" fill="none" stroke="var(--teal)" stroke-width="2"/><path d="M4 32V22q0-5 8-5t6 5q-2-5 6-5t8 5v10z" fill="none" stroke="var(--teal)" stroke-width="2"/></svg>
      <svg class="value-arrow" viewBox="0 0 28 12"><path d="M0 0 L28 6 L0 12 L5 6 Z" fill="var(--teal)"/></svg>Mate-ship relationships
    </li>
  </ul>

  <div class="digital-badge">
    <div class="percent">100%</div>
    <div style="height:66px"></div>
    <div class="label">Online Digital</div>
  </div>

  <div class="phone-mockup" role="img" aria-label="Mobile phone showing the payment home screen"></div>

  <section class="steps">
    <h2>To pay online, just follow three steps:</h2>
    <ol>
      <li><span class="num">1.</span>Visit swifttee.com.au</li>
      <li><span class="num">2.</span>Select club</li>
      <li><span class="num">3.</span>Confirm payment</li>
    </ol>
  </section>

  <p class="slogan">No Cash-No Worries</p>
  <div class="url-pill">swifttee.com.au</div>
</main>
</body>
</html>
```